Youth deer hunt give away flyer.

We need a flyer designed for a youth deer hunt giveaway that we are doing. We are an Illinois whitetail deer hunting outfitter. We house and feed our clients as well as providing them with a guided deer hunt. It needs to include images as well as details about the giveaway. Im looking for a proffesional, looking flyer

Target Market(s)

rednecks, hunters

Industry/Entity Type

Hunting

Font styles to use
Serif
Sans Serif

Colors
000000
dbdbdb
ffffff
474747

Requirements
Must have
• not sure
Nice to have
• not sure
Should not have
• not sure

```html
<!DOCTYPE html>
<html lang="en">
<head>
<meta charset="utf-8">
<title>2018 Youth Firearm Hunt – Harlan Ridge Outfitting</title>
<link rel="stylesheet" href="https://fonts.googleapis.com/css2?family=Cinzel:wght@400;600&family=Open+Sans:wght@400;600;700&display=swap">
<style>
  :root {
    --black: #000000;
    --light: #dbdbdb;
    --white: #ffffff;
    --charcoal: #474747;
    --orange: #ef7a2c;
    --ink: #2a2a2a;
    --stage: #e9e9e9;
  }
  html, body {
    margin: 0;
    width: 1200px;
    height: 1200px;
    overflow: hidden;
    background: var(--stage);
  }
  .flyer {
    position: absolute;
    left: 173px;
    top: 0;
    width: 982px;
    height: 1380px;
    transform: scale(0.8696);
    transform-origin: 0 0;
    background: var(--white);
    overflow: hidden;
    font-family: "Open Sans", Arial, sans-serif;
  }
  .flyer-header {
    position: absolute;
    left: 0;
    top: 0;
    width: 982px;
    height: 800px;
  }
  .brand-name {
    position: absolute;
    left: 315px;
    top: 676px;
    width: 361px;
    margin: 0;
    text-align: center;
    font-family: "Cinzel", Georgia, serif;
    font-weight: 400;
    color: var(--white);
    font-size: 34px;
    line-height: 38px;
    letter-spacing: 1px;
    white-space: nowrap;
  }
  .brand-sub {
    position: absolute;
    left: 315px;
    top: 722px;
    width: 361px;
    margin: 0;
    text-align: center;
    font-family: "Cinzel", Georgia, serif;
    font-weight: 400;
    color: var(--white);
    font-size: 14px;
    line-height: 18px;
    letter-spacing: 4px;
  }
  .info-area {
    position: absolute;
    left: 0;
    top: 690px;
    width: 982px;
    height: 371px;
    background: linear-gradient(180deg, #e4e4e4 0%, #ececec 55%, #e2e2e2 100%);
    z-index: -1;
  }
  .hunt-title {
    position: absolute;
    top: 790px;
    left: 0;
    width: 982px;
    margin: 0;
    text-align: center;
    font-family: "Cinzel", Georgia, serif;
    font-weight: 400;
    font-size: 54px;
    color: var(--orange);
  }
  .hunt-date {
    position: absolute;
    top: 857px;
    left: 0;
    width: 982px;
    margin: 0;
    text-align: center;
    font-weight: 600;
    font-size: 44px;
    color: var(--black);
  }
  .about {
    position: absolute;
    left: 40px;
    width: 902px;
    margin: 0;
    text-align: center;
    font-size: 14.5px;
    line-height: 19.5px;
    color: var(--ink);
  }
  .about-story { top: 926px; }
  .about-services { top: 1003px; }
  .offer-band {
    position: absolute;
    left: 0;
    top: 1061px;
    width: 982px;
    height: 136px;
    background: var(--black);
  }
  .offer-band svg { position: absolute; left: 0; top: 0; }
  .offer-label {
    position: absolute;
    left: 45px;
    top: 43px;
    margin: 0;
    font-family: "Cinzel", Georgia, serif;
    font-weight: 400;
    font-size: 41px;
    color: var(--white);
    letter-spacing: 1px;
  }
  .offer-list {
    position: absolute;
    left: 382px;
    top: 14px;
    width: 580px;
    margin: 0;
    padding: 0;
    list-style: none;
  }
  .offer-list li {
    position: relative;
    padding-left: 29px;
    margin-bottom: 7px;
    font-weight: 700;
    font-size: 16.5px;
    line-height: 23px;
    color: var(--white);
  }
  .offer-list li svg { position: absolute; left: 0; top: 4px; }
  .permit-note {
    position: absolute;
    left: 0;
    top: 1197px;
    width: 982px;
    height: 60px;
    margin: 0;
    background: #ececec;
    text-align: center;
    font-family: "Cinzel", Georgia, serif;
    font-weight: 400;
    font-size: 25px;
    line-height: 60px;
    letter-spacing: 1.5px;
    color: var(--black);
  }
  .contact-bar {
    position: absolute;
    left: 0;
    top: 1257px;
    width: 982px;
    height: 123px;
    background: var(--charcoal);
    color: var(--white);
    font-weight: 700;
  }
  .contact-item { position: absolute; display: flex; gap: 10px; white-space: nowrap; }
  .contact-address { left: 52px; top: 22px; font-size: 17px; line-height: 23px; }
  .contact-phone { left: 378px; top: 40px; font-size: 21px; align-items: center; }
  .contact-mail { left: 618px; top: 21px; font-size: 17px; align-items: center; }
  .contact-web { left: 618px; top: 66px; font-size: 17px; align-items: center; }
  .contact-mail svg, .contact-web svg { margin-right: 12px; }
</style>
</head>
<body>
<main class="flyer">
  <div class="info-area"></div>

  <svg class="flyer-header" viewBox="0 0 982 800" width="982" height="800">
    <defs>
      <linearGradient id="heroTone" x1="0" y1="0" x2="0" y2="1">
        <stop offset="0" stop-color="#eceeee"/>
        <stop offset="0.5" stop-color="#b9b1a3"/>
        <stop offset="0.75" stop-color="#7a5a36"/>
        <stop offset="1" stop-color="#6f7a4a"/>
      </linearGradient>
      <linearGradient id="cabinTone" x1="0" y1="0" x2="0" y2="1">
        <stop offset="0" stop-color="#e6e9ea"/>
        <stop offset="0.45" stop-color="#8a4a2a"/>
        <stop offset="0.7" stop-color="#5f7f36"/>
        <stop offset="1" stop-color="#4e7a2c"/>
      </linearGradient>
      <linearGradient id="interiorTone" x1="0" y1="0" x2="1" y2="1">
        <stop offset="0" stop-color="#b86a34"/>
        <stop offset="0.6" stop-color="#9a5426"/>
        <stop offset="1" stop-color="#6b3a1c"/>
      </linearGradient>
    </defs>
    <polygon points="0,0 982,0 982,350 490,484 0,345" fill="url(#heroTone)" role="img" aria-label="Photo of a young hunter in camouflage and orange cap posing beside a trophy whitetail buck"/>
    <polygon points="0,390 310,452 310,728 0,676" fill="url(#cabinTone)" role="img" aria-label="Photo of the log guest cabin with green roof on a grassy lawn"/>
    <polygon points="685,452 982,386 982,672 685,726" fill="url(#interiorTone)" role="img" aria-label="Photo of the cabin's wood-panelled kitchen interior with bar stools"/>
    <polygon points="0,676 310,730 490,764 685,728 982,672 982,692 490,788 0,698" fill="var(--charcoal)"/>
    <polygon points="308,446 683,446 683,734 495,780 308,734" fill="var(--white)"/>
    <polygon points="315,452 676,452 676,728 495,770 315,728" fill="var(--charcoal)"/>
    <circle cx="495" cy="582" r="62" fill="none" stroke="var(--white)" stroke-width="4"/>
  </svg>
  <p class="brand-name">Harlan Ridge</p>
  <p class="brand-sub">OUTFITTING</p>

  <h1 class="hunt-title">2018 Youth Firearm Hunt</h1>
  <p class="hunt-date">October 6-8, 2018</p>

  <p class="about about-story">Harlan Ridge Outfitting is a family owned and operated deer hunting outfitter located in Morgan and Scott Counties in west central Illinois. We provide low pressure, trophy whitetail hunts on privately owned farms across the region. The Harlans are lifelong residents and hunters of Morgan County, with the family farm being established well over 150 years ago.</p>
  <p class="about about-services">To go along with guiding deer and turkey hunters, we also offer a wide variety of professional hunting services that include whitetail land consulting, scouting services, CRP and food plot plantings and more</p>

  <section class="offer-band">
    <svg width="320" height="136" viewBox="0 0 320 136">
      <polygon points="0,0 258,0 310,68 258,136 0,136" fill="var(--charcoal)"/>
      <polyline points="258,0 310,68 258,136" fill="none" stroke="var(--white)" stroke-width="8"/>
    </svg>
    <h2 class="offer-label">We Offer</h2>
    <ul class="offer-list">
      <li><svg width="16" height="16" viewBox="0 0 16 16"><circle cx="8" cy="8" r="7" fill="none" stroke="#555" stroke-width="1.5"/><path d="M4.5 8.2l2.4 2.3 4.6-5" fill="none" stroke="#555" stroke-width="1.6"/></svg>4 night stay in our private cabin that include meals for 2 parents and the child.</li>
      <li><svg width="16" height="16" viewBox="0 0 16 16"><circle cx="8" cy="8" r="7" fill="none" stroke="#555" stroke-width="1.5"/><path d="M4.5 8.2l2.4 2.3 4.6-5" fill="none" stroke="#555" stroke-width="1.6"/></svg>Guided shotgun hunt on strictly managed properties.</li>
      <li><svg width="16" height="16" viewBox="0 0 16 16"><circle cx="8" cy="8" r="7" fill="none" stroke="#555" stroke-width="1.5"/><path d="M4.5 8.2l2.4 2.3 4.6-5" fill="none" stroke="#555" stroke-width="1.6"/></svg>Ground blinds in place</li>
    </ul>
  </section>

  <p class="permit-note">Permit and license fees are the hunters responsibility</p>

  <footer class="contact-bar">
    <div class="contact-item contact-address">
      <svg width="16" height="22" viewBox="0 0 16 22"><path d="M8 1a7 7 0 0 0-7 7c0 5 7 13 7 13s7-8 7-13a7 7 0 0 0-7-7z" fill="var(--black)"/><circle cx="8" cy="8" r="2.6" fill="var(--charcoal)"/></svg>
      <div>Wade Harlan<br>1840 Ridge Road<br>Milford Grove, Illinois 62699</div>
    </div>
    <div class="contact-item contact-phone">
      <svg width="22" height="22" viewBox="0 0 24 24"><path d="M6.6 10.8a15 15 0 0 0 6.6 6.6l2.2-2.2c.3-.3.7-.4 1-.2 1.1.4 2.3.6 3.6.6.6 0 1 .4 1 1V20c0 .6-.4 1-1 1A17 17 0 0 1 3 4c0-.6.4-1 1-1h3.5c.6 0 1 .4 1 1 0 1.3.2 2.5.6 3.6.1.3 0 .7-.2 1z" fill="var(--black)"/></svg>
      <span>(217)555-0148</span>
    </div>
    <div class="contact-item contact-mail">
      <svg width="26" height="18" viewBox="0 0 26 18"><rect x="0" y="0" width="26" height="18" fill="var(--black)"/><path d="M1 1l12 9 12-9" fill="none" stroke="var(--charcoal)" stroke-width="2"/></svg>
      <span>harlanridgeoutfitting@mailbox.com</span>
    </div>
    <div class="contact-item contact-web">
      <svg width="26" height="26" viewBox="0 0 26 26"><g fill="none" stroke="var(--black)" stroke-width="2.2"><circle cx="13" cy="13" r="11"/><ellipse cx="13" cy="13" rx="5" ry="11"/><path d="M2 13h22M4 7h18M4 19h18"/></g></svg>
      <span>www.harlanridgeoutfitting.com</span>
    </div>
  </footer>
</main>
</body>
</html>
```